Medical Practice Business Card

we need a business card for our new medical ophthalmology practice based in Needham Massachusetts. we are looking for a simple , modern and elegant design.
the card needs to contain the following
1- the logo of our practice (please see attached file)
2- the name of the practice : "Silver Birch Retina Care"
3- Doctor's Name: Tobias Rendell MD PhD
4- Specialty: Board-Certified Vitreoretinal Surgeon
5- practice address: 87 Larkspur Ave, Suite 210, Needham MA 02481
7- Office number: 617- 482 - 7730
8- fax number: 617- 391 - 2268
9- email: info@sbretinahub.example
10- website: www.sbretinahub.example

```html
<!DOCTYPE html>
<html lang="en">
<head>
<meta charset="utf-8">
<title>Silver Birch Retina Care – Business Card</title>
<link rel="stylesheet" href="https://fonts.googleapis.com/css2?family=Cinzel:wght@600;700&family=Tinos:wght@400;700&display=swap">
<style>
  :root {
    --bg: #e3e4e6;
    --card: #ffffff;
    --navy: #0d2a5c;
    --royal: #1557b0;
    --sky: #7ccfe0;
    --ink: #333a44;
    --grey: #555b63;
  }
  * { box-sizing: border-box; margin: 0; padding: 0; }
  html, body { width: 1200px; height: 800px; overflow: hidden; }
  body {
    background: var(--bg);
    position: relative;
    font-family: "Tinos", "Times New Roman", serif;
  }
  .card {
    position: absolute;
    top: 245px;
    width: 540px;
    height: 310px;
    background: var(--card);
    overflow: hidden;
    box-shadow: 0 6px 18px rgba(0,0,0,0.12);
  }
  .card--front { left: 40px; }
  .card--back { left: 620px; }
  .card__bands { position: absolute; inset: 0; }

  .website-line {
    position: absolute;
    left: 34px; top: 30px;
    font-family: "Tinos", serif;
    font-weight: 700;
    font-size: 17px;
    letter-spacing: 3.2px;
    color: var(--ink);
  }
  .website-line .accent { color: var(--sky); }

  .practice-name {
    position: absolute;
    font-family: "Cinzel", serif;
    font-weight: 700;
    color: var(--navy);
    line-height: 1.05;
    text-align: left;
  }
  .card--front .practice-name { right: 40px; top: 130px; font-size: 27px; }
  .card--back .practice-name { right: 30px; top: 34px; font-size: 21px; }
  .practice-name .mark {
    display: inline-block;
    width: 12px; height: 12px;
    border-radius: 50%;
    background: var(--royal);
    margin-right: 8px;
    vertical-align: middle;
  }

  .header-rule { position: absolute; left: 20px; top: 22px; }

  .contact-list {
    position: absolute;
    left: 22px; top: 58px;
    list-style: none;
    font-size: 13px;
    color: var(--ink);
  }
  .contact-list li {
    display: flex;
    align-items: center;
    gap: 7px;
    height: 19px;
  }
  .contact-list svg { width: 13px; height: 13px; flex: none; }

  .doctor {
    position: absolute;
    right: 30px; top: 88px;
    text-align: right;
  }
  .doctor__name {
    font-family: "Cinzel", serif;
    font-weight: 700;
    font-size: 15.5px;
    color: var(--navy);
    letter-spacing: 0.3px;
  }
  .doctor__title {
    margin-top: 3px;
    font-size: 14px;
    color: var(--grey);
  }
</style>
</head>
<body>

  <section class="card card--front" aria-label="Card front">
    <p class="website-line">www.<span class="accent">sbretinahub</span>.example</p>

    <svg class="card__bands" viewBox="0 0 540 310" aria-hidden="true">
      <rect x="0" y="208" width="200" height="36" fill="var(--royal)"/>
      <rect x="178" y="232" width="400" height="52" rx="16" fill="var(--card)"/>
      <rect x="184" y="238" width="400" height="40" rx="14" fill="var(--sky)"/>
    </svg>

    <h1 class="practice-name"><span class="mark"></span>Silver Birch<br>Retina Care</h1>
  </section>

  <section class="card card--back" aria-label="Card back">
    <svg class="header-rule" width="320" height="50" viewBox="0 0 320 50" aria-hidden="true">
      <circle cx="8" cy="8" r="7" fill="none" stroke="var(--sky)" stroke-width="1.2"/>
      <line x1="15" y1="9" x2="312" y2="30" stroke="var(--sky)" stroke-width="0.8"/>
    </svg>

    <ul class="contact-list">
      <li>
        <svg viewBox="0 0 16 16" aria-hidden="true"><rect x="3" y="1" width="10" height="5" fill="none" stroke="var(--sky)" stroke-width="1.4"/><rect x="1" y="6" width="14" height="7" rx="1.5" fill="var(--sky)"/><rect x="4" y="10" width="8" height="5" fill="#fff" stroke="var(--sky)" stroke-width="1.2"/></svg>
        617- 391 - 2268
      </li>
      <li>
        <svg viewBox="0 0 16 16" aria-hidden="true"><path d="M4 1.5l2.5 3-1.5 1.6c.8 1.8 2.2 3.3 4 4.2l1.6-1.5 3 2.4-1.6 2.8C7 13.5 2.5 9 1.6 3.2z" fill="var(--sky)"/></svg>
        617- 482 - 7730
      </li>
      <li>
        <svg viewBox="0 0 16 16" aria-hidden="true"><rect x="1" y="3" width="14" height="10" fill="none" stroke="var(--sky)" stroke-width="1.4"/><path d="M1 3l7 6 7-6" fill="none" stroke="var(--sky)" stroke-width="1.4"/></svg>
        info@sbretinahub.example
      </li>
      <li>
        <svg viewBox="0 0 16 16" aria-hidden="true"><circle cx="8" cy="8" r="6.5" fill="none" stroke="var(--sky)" stroke-width="1.3"/><ellipse cx="8" cy="8" rx="3" ry="6.5" fill="none" stroke="var(--sky)" stroke-width="1.1"/><line x1="1.5" y1="8" x2="14.5" y2="8" stroke="var(--sky)" stroke-width="1.1"/></svg>
        www.sbretinahub.example
      </li>
      <li>
        <svg viewBox="0 0 16 16" aria-hidden="true"><path d="M8 15s5-5.5 5-9A5 5 0 0 0 3 6c0 3.5 5 9 5 9z" fill="var(--sky)"/><circle cx="8" cy="6" r="1.8" fill="#fff"/></svg>
        87 Larkspur Ave, Suite 210, Needham MA 02481
      </li>
    </ul>

    <h2 class="practice-name"><span class="mark"></span>Silver Birch<br>Retina Care</h2>

    <div class="doctor">
      <p class="doctor__name">Tobias Rendell MD PhD</p>
      <p class="doctor__title">Certified Vitreoretinal Surgeon</p>
    </div>

    <svg class="card__bands" viewBox="0 0 540 310" aria-hidden="true">
      <rect x="-20" y="168" width="355" height="44" rx="16" fill="var(--sky)"/>
      <rect x="312" y="200" width="240" height="50" rx="14" fill="var(--card)"/>
      <rect x="318" y="206" width="240" height="38" fill="var(--royal)"/>
    </svg>
  </section>

</body>
</html>
```